Book Cover - The Velvet Lantern Almanac Collection

We are writing a book about the velvet lantern almanac collection, including Guerrilla Marketing. Advertising, Branding and PR.

We are looking for a fun and quirky cover, and are open to your ideas 💡
My website and social media are on www.TorvanPelica.co and posts are shared on Trelvano. Again we are open to ideas

```html
<!DOCTYPE html>
<html lang="en">
<head>
<meta charset="utf-8">
<title>The Velvet Lantern Almanac Collection — Book Cover</title>
<link rel="stylesheet" href="https://fonts.googleapis.com/css2?family=Bebas+Neue&family=Outfit:wght@400;500&display=swap">
<style>
  :root {
    --page-white: #ffffff;
    --cover-yellow: #EBC63E;
    --accent-orange: #EB5324;
    --ink-black: #0A0A0A;
    --type-white: #ffffff;
  }
  html, body {
    margin: 0;
    padding: 0;
    width: 1200px;
    height: 1200px;
    overflow: hidden;
    background: var(--page-white);
  }
  .book-cover {
    position: absolute;
    left: 221px;
    top: 31px;
    width: 758px;
    height: 1137px;
    background: var(--cover-yellow);
    overflow: hidden;
  }
  .title-block {
    position: absolute;
    left: 0;
    top: 0;
    width: 758px;
    height: 500px;
  }
  .title-block text {
    font-family: "Bebas Neue", "Oswald", sans-serif;
  }
  .title-band { fill: var(--accent-orange); }
  .title-kicker { fill: var(--type-white); font-size: 96px; }
  .title-main { fill: var(--type-white); font-size: 184px; }
  .title-tail { fill: var(--ink-black); font-size: 190px; }

  .hero-artwork {
    position: absolute;
    left: 89px;
    top: 517px;
    width: 580px;
    height: 315px;
    border-radius: 150px 60px 40px 120px;
    background: var(--accent-orange);
  }
  .subtitle {
    position: absolute;
    left: 0;
    top: 880px;
    width: 758px;
    margin: 0;
    text-align: center;
    font-family: "Outfit", "Helvetica Neue", Arial, sans-serif;
    font-weight: 400;
    font-size: 36px;
    line-height: 45px;
    color: var(--ink-black);
  }
  .author-band {
    position: absolute;
    left: 0;
    bottom: 0;
    width: 758px;
    height: 86px;
    background: var(--accent-orange);
    display: flex;
    align-items: center;
    justify-content: center;
  }
  .author-name {
    font-family: "Outfit", "Helvetica Neue", Arial, sans-serif;
    font-weight: 500;
    font-size: 50px;
    letter-spacing: 2px;
    color: var(--type-white);
  }
</style>
</head>
<body>
  <main class="book-cover">
    <svg class="title-block" viewBox="0 0 758 500" role="heading" aria-level="1" aria-label="The Velvet Lantern Almanac Collection">
      <rect class="title-band" x="45" y="60" width="499" height="98"/>
      <rect class="title-band" x="508" y="60" width="36" height="248"/>
      <text class="title-kicker" x="66" y="142" textLength="420" lengthAdjust="spacingAndGlyphs">THE VELVET LANTERN</text>
      <text class="title-main" x="45" y="308" textLength="448" lengthAdjust="spacingAndGlyphs">ALMANAC</text>
      <text class="title-tail" x="45" y="456" textLength="650" lengthAdjust="spacingAndGlyphs">COLLECTION</text>
    </svg>

    <div class="hero-artwork" role="img" aria-label="Flat orange figure shouting into a megaphone with sound lines"></div>

    <p class="subtitle">Featuring Guerrilla Marketing,<br>Branding, PR, and More</p>

    <footer class="author-band">
      <span class="author-name">AUTHOR NAME</span>
    </footer>
  </main>
</body>
</html>
```